Dean Hollis Business Card

In addition to my name design (file uploaded), black print on white card stock, e-mail address should be presented as a typical e-mail address, i.e., underlined and in blue ink, the card should include the following information:
Professor of Aviation Technology
Accident Litigation Expert Witness
Master Certificated Flight Instructor

dhollis@vexmail.example
Anchorage, Alaska
(907) 318-5074

```html
<!DOCTYPE html>
<html lang="en">
<head>
<meta charset="utf-8">
<title>Dean Hollis Business Card</title>
<link rel="stylesheet" href="https://fonts.googleapis.com/css2?family=Oswald:wght@500&family=Roboto+Condensed:wght@400&display=swap">
<style>
  :root {
    --page-bg: #e9e9ea;
    --card-bg: #ffffff;
    --ink: #111111;
    --accent-blue: #6a78cc;
    --link-blue: #3f55c8;
  }
  * { box-sizing: border-box; margin: 0; padding: 0; }
  html, body {
    width: 1200px;
    height: 1000px;
    overflow: hidden;
    background: var(--page-bg);
  }
  .business-card {
    position: absolute;
    left: 150px;
    top: 243px;
    width: 900px;
    height: 514px;
    background: var(--card-bg);
    box-shadow: 0 6px 24px rgba(0,0,0,0.18);
    overflow: hidden;
  }
  .card-rules {
    position: absolute;
    inset: 0;
    width: 900px;
    height: 514px;
  }
  .name-mark {
    position: absolute;
    left: 60px;
    top: 168px;
    font-family: "Oswald", sans-serif;
    font-weight: 500;
    font-size: 50px;
    letter-spacing: 3px;
    color: var(--ink);
    line-height: 1;
  }
  .plane-mark {
    position: absolute;
    left: 400px;
    top: 210px;
    width: 72px;
    height: 72px;
    border-radius: 50%;
    background: var(--ink);
  }
  .credentials {
    position: absolute;
    left: 520px;
    top: 150px;
    font-family: "Roboto Condensed", sans-serif;
    font-size: 22px;
    line-height: 1.18;
    color: var(--ink);
    letter-spacing: 0.5px;
  }
  .contact {
    position: absolute;
    right: 48px;
    top: 290px;
    text-align: right;
    font-family: "Roboto Condensed", sans-serif;
    font-size: 22px;
    line-height: 1.25;
    color: var(--ink);
    letter-spacing: 0.5px;
    font-style: normal;
  }
  .contact .email {
    color: var(--link-blue);
    text-decoration: underline;
    text-underline-offset: 4px;
  }
</style>
</head>
<body>
  <div class="business-card">
    <svg class="card-rules" viewBox="0 0 900 514" aria-hidden="true">
      <!-- upper divider -->
      <line x1="436" y1="0" x2="436" y2="200" stroke="var(--ink)" stroke-width="3"/>
      <line x1="422" y1="40" x2="422" y2="200" stroke="var(--accent-blue)" stroke-width="7"/>
      <line x1="450" y1="40" x2="450" y2="200" stroke="var(--accent-blue)" stroke-width="7"/>
      <!-- lower divider -->
      <line x1="436" y1="292" x2="436" y2="514" stroke="var(--ink)" stroke-width="3"/>
      <line x1="422" y1="292" x2="422" y2="450" stroke="var(--accent-blue)" stroke-width="7"/>
      <line x1="450" y1="292" x2="450" y2="450" stroke="var(--accent-blue)" stroke-width="7"/>
      <!-- horizontal rule -->
      <line x1="472" y1="246" x2="900" y2="270" stroke="var(--ink)" stroke-width="3"/>
    </svg>

    <h1 class="name-mark">DEAN E. HOLLIS</h1>

    <div class="plane-mark" role="img" aria-label="Airplane silhouette seen from above"></div>

    <div class="credentials">
      <p>Professor of Aviation Technology</p>
      <p>Accident Litigation Expert Witness</p>
      <p>Master Certificated Flight Instructor</p>
    </div>

    <address class="contact">
      <p>Anchorage, Alaska</p>
      <p>T: (907) 318-5074</p>
      <p class="email">E: dhollis@vexmail.example</p>
    </address>
  </div>
</body>
</html>
```